Premium label design for product needed

UPDATE: (Scroll down)
For a face care product i need a new front label on the bottle. The current one is white and i want to add the franchise color green. The objective is to premiunize the packaging and to give guidance to the consumers to find their franchise color. The task is to find several option to color the label on the bottle in the most premium way. But at the same time it should not be playful, more in a serious medical direction or in a counterbrand direction. It should look absolutely premium. but should not shout to much. The text structure should remain the same. I will provide a powerpoint slide to illustrate the task even clearer.
UPDATE: DO NOT DESIGN THE FOLDING BOX, only design the bottle. The folding box only serves the purpose of giving the text/layout structure and rough color intent.

Target Market(s)

female 25-39

Requirements
Must have
• Premium, Uniqueness, Innovative

```html
<!DOCTYPE html>
<html lang="en">
<head>
<meta charset="utf-8">
<title>Calmera Face Care – Bottle Label Options</title>
<link rel="stylesheet" href="https://fonts.googleapis.com/css2?family=Libre+Baskerville:wght@400;700&family=Patrick+Hand&display=swap">
<style>
  :root {
    --page-bg: #ececec;
    --franchise-green: #8fc9a0;
    --green-light: #b4dfc0;
    --ink: #1e1e1e;
    --silver-dark: #9a9a9a;
    --silver-light: #f4f4f4;
    --frame-white: #ffffff;
  }
  html, body {
    margin: 0;
    padding: 0;
    width: 1200px;
    height: 800px;
    overflow: hidden;
    background: var(--page-bg);
  }
  .board { display: block; width: 1200px; height: 800px; }
  .brand-name {
    font-family: "Libre Baskerville", Georgia, serif;
    font-weight: 400;
    font-size: 17px;
    fill: var(--ink);
  }
  .brand-line {
    font-family: "Libre Baskerville", Georgia, serif;
    font-size: 8px;
    font-style: italic;
    fill: var(--ink);
  }
  .product-name {
    font-family: "Libre Baskerville", Georgia, serif;
    font-size: 7.5px;
    fill: var(--ink);
  }
  .option-letter {
    font-family: "Patrick Hand", "Comic Sans MS", cursive;
    font-size: 34px;
    fill: var(--ink);
  }
  .label-band { fill: url(#labelGreen); }
  .silver { fill: url(#silverEdge); }
  .silver-line { fill: none; stroke: url(#silverEdge); stroke-width: 3; }
  .label-frame { fill: none; stroke: var(--frame-white); stroke-width: 1.5; }
</style>
</head>
<body>
<svg class="board" viewBox="0 0 1200 800" xmlns="http://www.w3.org/2000/svg">
  <defs>
    <linearGradient id="capMetal" x1="0" x2="1" y1="0" y2="0">
      <stop offset="0" stop-color="#e4e4e4"/>
      <stop offset="0.25" stop-color="#f7f7f7"/>
      <stop offset="0.7" stop-color="#a8a8a8"/>
      <stop offset="1" stop-color="#dcdcdc"/>
    </linearGradient>
    <linearGradient id="bodyWhite" x1="0" x2="1" y1="0" y2="0">
      <stop offset="0" stop-color="#dedede"/>
      <stop offset="0.3" stop-color="#fafafa"/>
      <stop offset="0.75" stop-color="#e6e6e6"/>
      <stop offset="1" stop-color="#d4d4d4"/>
    </linearGradient>
    <linearGradient id="labelGreen" x1="0" x2="1" y1="0" y2="0">
      <stop offset="0" stop-color="#8cc6a0"/>
      <stop offset="0.6" stop-color="var(--franchise-green)"/>
      <stop offset="0.85" stop-color="var(--green-light)"/>
      <stop offset="1" stop-color="#8cc6a0"/>
    </linearGradient>
    <linearGradient id="silverEdge" x1="0" x2="1" y1="0" y2="0">
      <stop offset="0" stop-color="var(--silver-dark)"/>
      <stop offset="0.5" stop-color="var(--silver-light)"/>
      <stop offset="1" stop-color="var(--silver-dark)"/>
    </linearGradient>
    <g id="bottleShell">
      <rect x="0" y="178" width="137" height="146" fill="url(#capMetal)"/>
      <path d="M0 324 H137 V615 Q137 623 129 623 H8 Q0 623 0 615 Z" fill="url(#bodyWhite)"/>
      <line x1="0" y1="324" x2="137" y2="324" stroke="#cfcfcf" stroke-width="1"/>
    </g>
    <g id="labelText">
      <text class="brand-name" x="68.5" y="440" text-anchor="middle">Calmera</text>
      <text class="brand-line" x="68.5" y="454" text-anchor="middle">face care</text>
      <text class="product-name" x="68.5" y="548" text-anchor="middle">B.K. SOFT FLUID</text>
    </g>
  </defs>

  <!-- Option I: inner frame with offset silver tabs -->
  <g class="bottle option-i" transform="translate(93 0)">
    <use href="#bottleShell"/>
    <rect class="label-band" x="0" y="385" width="137" height="115"/>
    <rect class="label-frame" x="7" y="396" width="120" height="96"/>
    <rect class="silver" x="131" y="386" width="6" height="48"/>
    <rect class="silver" x="0" y="432" width="6" height="68"/>
    <use href="#labelText"/>
  </g>

  <!-- Option J: curved silver edges top and bottom -->
  <g class="bottle option-j" transform="translate(313 0)">
    <use href="#bottleShell"/>
    <rect class="label-band" x="0" y="383" width="137" height="115"/>
    <path class="silver" d="M0 383 Q68.5 395 137 383 L137 389 Q68.5 401 0 389 Z"/>
    <path class="silver" d="M0 498 Q68.5 486 137 498 L137 492 Q68.5 480 0 492 Z"/>
    <use href="#labelText"/>
  </g>

  <!-- Option K: silver corner bracket -->
  <g class="bottle option-k" transform="translate(540 0)">
    <use href="#bottleShell"/>
    <rect class="label-band" x="0" y="384" width="137" height="115"/>
    <polyline class="silver-line" points="17,472 17,404 112,404"/>
    <use href="#labelText"/>
  </g>

  <!-- Option L: silver edge tabs right-top and left-bottom -->
  <g class="bottle option-l" transform="translate(762 0)">
    <use href="#bottleShell"/>
    <rect class="label-band" x="0" y="381" width="137" height="115"/>
    <rect class="silver" x="131" y="382" width="6" height="52"/>
    <rect class="silver" x="0" y="428" width="6" height="68"/>
    <use href="#labelText"/>
  </g>

  <!-- Option M: single silver tab on the right -->
  <g class="bottle option-m" transform="translate(968 0)">
    <use href="#bottleShell"/>
    <rect class="label-band" x="0" y="383" width="137" height="115"/>
    <rect class="silver" x="132" y="405" width="6" height="62"/>
    <use href="#labelText"/>
  </g>

  <text class="option-letter" x="151" y="685" text-anchor="middle">I</text>
  <text class="option-letter" x="391" y="685" text-anchor="middle">J</text>
  <text class="option-letter" x="613" y="685" text-anchor="middle">K</text>
  <text class="option-letter" x="835" y="685" text-anchor="middle">L</text>
  <text class="option-letter" x="1040" y="680" text-anchor="middle">M</text>
</svg>
</body>
</html>
```